Business Cards for cafe providing speciality coffee and food

I need a business card design for my husband’s businesses. He has two cafes in Brisbane. The business name is Copperleaf Roasting House. They sell high end specialty coffee as well as breakfast and lunch. All the food is cooked fresh, in house and they have strict quality controls for their coffee. I would like the business card to feature the address for both cafes, my husband’s phone number and the business’s instagram. The address for the first is 61 Wexley Crescent, Pine Hollow and the second is 23 Dorrit Avenue, Sallowmere. The Instagram handle is @copperleafroastinghouse and phone number is 0491326085. We already have a business logo that is attached.

Target Market(s)

All ages, higher disposable income and more likely to eat out regularly

Industry/Entity Type

Hospitality

Contact Information for Business Card

Must be suitable for both customers and suppliers

Font styles to use
Sans Serif

Colors

Designer to choose colors to be used in the design.

Requirements
Must have
• Owner’s name: Griff Tallant
• Addresses of both cafes: 61 Wexley Crescent, Pine Hollow and 23 Dorrit Avenue, Sallowmere
• Instagram handle: @copperleafroastinghouse
• Contact number: 0491326085
Nice to have
• Business logo

```html
<!DOCTYPE html>
<html lang="en">
<head>
<meta charset="utf-8">
<title>Copperleaf Roasting House – Business Card</title>
<link rel="stylesheet" href="https://fonts.googleapis.com/css2?family=Montserrat:wght@400;500&family=Poiret+One&display=swap">
<style>
  :root {
    --backdrop: #d9d9d9;
    --slate: #3a4042;
    --slate-deep: #2c3133;
    --paper: #ffffff;
    --ink: #1c1c1c;
    --roast: #4b2f25;
    --chalk: #f1f1f1;
  }
  * { box-sizing: border-box; margin: 0; padding: 0; }
  html, body {
    width: 1200px; height: 900px; overflow: hidden;
    background: var(--backdrop);
  }
  .sheet {
    width: 1200px; height: 900px;
    display: flex; align-items: center; justify-content: center; gap: 40px;
  }
  .card {
    width: 540px; height: 309px; position: relative; overflow: hidden;
    box-shadow: 0 6px 18px rgba(0,0,0,0.18);
  }

  /* Back side */
  .card--back {
    background: linear-gradient(160deg, var(--slate) 0%, var(--slate-deep) 100%);
    display: flex; align-items: center; justify-content: center;
  }
  .brand-mark {
    display: flex; flex-direction: column; align-items: center; gap: 14px;
  }
  .brand-mark__dot {
    width: 22px; height: 22px; border-radius: 50%; background: var(--chalk);
  }
  .brand-mark__name {
    font-family: "Montserrat", sans-serif; font-weight: 500;
    color: var(--chalk); font-size: 15px; letter-spacing: 3px;
    text-transform: uppercase; text-align: center; line-height: 1.6;
  }

  /* Front side */
  .card--front { background: var(--paper); }
  .engine-art {
    position: absolute; left: 34px; top: 0; width: 190px; height: 300px;
    background: radial-gradient(ellipse at 50% 45%, var(--roast) 0%, #6a4a3e 80%);
    border-radius: 30px 30px 95px 95px;
  }
  .contact {
    position: absolute; right: 28px; top: 110px; width: 290px;
    text-align: right; font-family: "Montserrat", sans-serif; color: var(--ink);
  }
  .contact__name {
    font-family: "Poiret One", sans-serif; font-size: 31px;
    letter-spacing: 2px; text-transform: uppercase; line-height: 1;
  }
  .contact__role {
    font-size: 11px; margin-top: 2px; margin-bottom: 12px;
  }
  .contact__list { list-style: none; }
  .contact__item {
    display: flex; justify-content: flex-end; align-items: center;
    gap: 7px; font-size: 11px; line-height: 1; margin-bottom: 7px;
  }
  .contact__icon { width: 13px; height: 13px; flex: none; }
  .contact__circle {
    width: 12px; height: 12px; border-radius: 50%; background: var(--ink); flex: none;
  }
</style>
</head>
<body>
<main class="sheet">
  <section class="card card--back" aria-label="Card back">
    <div class="brand-mark">
      <span class="brand-mark__dot"></span>
      <span class="brand-mark__name">Copperleaf<br>Roasting House</span>
    </div>
  </section>

  <section class="card card--front" aria-label="Card front">
    <div class="engine-art" role="img" aria-label="Distressed brown illustration of a steam locomotive front emerging from a cloud of steam"></div>
    <div class="contact">
      <h1 class="contact__name">Griff Tallant</h1>
      <p class="contact__role">Director</p>
      <ul class="contact__list">
        <li class="contact__item">
          <span>0491326085</span>
          <svg class="contact__icon" viewBox="0 0 16 16" aria-hidden="true"><circle cx="8" cy="8" r="8" fill="#1c1c1c"/><path d="M5.2 4.2l1.4-.3.8 2-1 .8a5.5 5.5 0 0 0 2.9 2.9l.8-1 2 .8-.3 1.4c-3.7.3-6.9-2.9-6.6-6.6z" fill="#fff"/></svg>
        </li>
        <li class="contact__item">
          <span>@copperleafroastinghouse</span>
          <span class="contact__circle"></span>
        </li>
        <li class="contact__item">
          <span>61 Wexley Crescent, Pine Hollow</span>
          <svg class="contact__icon" viewBox="0 0 16 16" aria-hidden="true"><path d="M8 1a4.5 4.5 0 0 0-4.5 4.5C3.5 9 8 15 8 15s4.5-6 4.5-9.5A4.5 4.5 0 0 0 8 1zm0 6.3a1.8 1.8 0 1 1 0-3.6 1.8 1.8 0 0 1 0 3.6z" fill="#1c1c1c"/></svg>
        </li>
        <li class="contact__item">
          <span>23 Dorrit Avenue, Sallowmere</span>
          <svg class="contact__icon" viewBox="0 0 16 16" aria-hidden="true"><path d="M8 1a4.5 4.5 0 0 0-4.5 4.5C3.5 9 8 15 8 15s4.5-6 4.5-9.5A4.5 4.5 0 0 0 8 1zm0 6.3a1.8 1.8 0 1 1 0-3.6 1.8 1.8 0 0 1 0 3.6z" fill="#1c1c1c"/></svg>
        </li>
      </ul>
    </div>
  </section>
</main>
</body>
</html>
```